Retainer Care Instructions

Please make this PDF - more modern and easy to read for patients. Our demographic is predominately adolescents. All the information is important and text needs to remain relatively the same - can be simplified. Here is a link to care instructions that look nice https://www.brightpath-grins.com/resources

Target Market(s)

Parents and Children

Industry/Entity Type

Orthodontics

Colors
0054AA
0677BA
7BADD7
CADEEF
E8F1F8

Requirements
Must have
• Simple and clear
Nice to have
• Add graphics and images to look more modern
Should not have
• Graphics to demonstrate

```html
<!DOCTYPE html>
<html lang="en">
<head>
<meta charset="utf-8">
<title>Retainer Care Instructions – Northbay Orthodontics</title>
<link href="https://fonts.googleapis.com/css2?family=Baloo+2:wght@800&family=Open+Sans:wght@700&family=Roboto+Condensed:wght@400;700&display=swap" rel="stylesheet">
<style>
  :root {
    --sky: #d4effd;
    --white: #ffffff;
    --title-blue: #0a9be3;
    --icon-blue: #0b98e0;
    --icon-tint: #cfeafa;
    --coral: #f4566e;
    --ink: #2b2b2b;
    --rule: #dcdcdc;
    --logo-grey: #b9b9b9;
    --illus-blue: #7ea8f2;
    --illus-grey: #b9b9b9;
    --warn-yellow: #ffea00;
  }
  * { box-sizing: border-box; margin: 0; padding: 0; }
  html, body { width: 849px; height: 1200px; overflow: hidden; }
  body { position: relative; background: var(--white); font-family: "Roboto Condensed", sans-serif; color: var(--ink); }

  .header-band { position: absolute; left: 0; top: 0; width: 849px; height: 207px; background: var(--sky); }
  .brand-box { position: absolute; left: 37px; top: 25px; width: 162px; height: 150px; background: var(--white); border-radius: 8px; display: flex; align-items: center; justify-content: center; text-align: center; }
  .brand-name { font-family: "Roboto Condensed", sans-serif; font-weight: 700; font-size: 22px; line-height: 1.15; color: var(--title-blue); }
  .page-title { position: absolute; left: 222px; top: 40px; width: 560px; text-align: center; font-family: "Baloo 2", sans-serif; font-weight: 800; font-size: 64px; line-height: 54px; color: var(--title-blue); letter-spacing: 0.3px; }

  .section-heading { font-family: "Open Sans", sans-serif; font-weight: 700; font-size: 29px; color: var(--coral); text-align: center; letter-spacing: 0.5px; }
  .care-heading { position: absolute; left: 0; top: 224px; width: 849px; }

  .care-item { position: absolute; display: flex; }
  .item-number { position: absolute; font-family: "Open Sans", sans-serif; font-weight: 700; font-size: 18px; color: var(--ink); }
  .item-icon { position: absolute; width: 68px; height: 72px; border-radius: 10px; background: var(--icon-tint); border: 2px solid var(--icon-blue); }
  .item-text { position: absolute; font-size: 16.5px; line-height: 22px; }
  .item-text b { font-weight: 700; }

  .rule { position: absolute; height: 2px; background: var(--rule); }

  .clean-band { position: absolute; left: 0; top: 771px; width: 849px; height: 429px; background: var(--sky); }
  .clean-tab { position: absolute; left: 198px; top: 735px; width: 452px; height: 40px; background: var(--white); border-radius: 18px 18px 0 0; }
  .clean-heading { position: absolute; left: 0; top: 739px; width: 849px; }

  .illustration { position: absolute; border-radius: 14px; }
  .soak-illus { left: 50px; top: 808px; width: 138px; height: 142px; background: linear-gradient(160deg, var(--illus-blue), var(--illus-grey)); }
  .rinse-illus { left: 488px; top: 805px; width: 100px; height: 145px; background: linear-gradient(200deg, var(--illus-grey), var(--illus-blue)); }
  .clean-text { position: absolute; font-size: 17.5px; line-height: 24px; }
  .clean-text b { font-weight: 700; }

  .warning-box { position: absolute; left: 44px; top: 986px; width: 761px; height: 179px; background: var(--white); border-radius: 26px; }
  .warning-icon { position: absolute; left: 290px; top: 997px; }
  .warning-heading { position: absolute; left: 362px; top: 1000px; font-family: "Open Sans", sans-serif; font-weight: 700; font-size: 25px; color: var(--coral); }
  .warning-list { position: absolute; left: 86px; top: 1046px; width: 700px; list-style: none; font-size: 16.5px; line-height: 23px; }
  .warning-list li { padding-left: 19px; text-indent: -19px; }
  .warning-list b { font-weight: 700; }
</style>
</head>
<body>
  <header>
    <div class="header-band"></div>
    <div class="brand-box"><span class="brand-name">Northbay<br>Orthodontics</span></div>
    <h1 class="page-title">The Braces Are Off<br>It's Retainer Time!</h1>
  </header>

  <section class="care">
    <h2 class="section-heading care-heading">HOW TO CARE FOR RETAINERS:</h2>

    <span class="item-number" style="left:23px;top:282px">1.</span>
    <div class="item-icon" role="img" aria-label="Orthodontist and tooth icon" style="left:50px;top:282px"></div>
    <p class="item-text" style="left:137px;top:282px;width:280px"><b>Wear your retainer as instructed:</b><br>Always wear your retainer as<br>instructed by your orthodontist</p>

    <span class="item-number" style="left:441px;top:278px">2.</span>
    <div class="item-icon" role="img" aria-label="Food, drink and football icon" style="left:467px;top:282px"></div>
    <p class="item-text" style="left:562px;top:282px;width:260px"><b>Remove retainer during meals and sports:</b> Take out your retainer when eating and playing sports.</p>

    <div class="rule" style="left:32px;top:374px;width:785px"></div>

    <span class="item-number" style="left:23px;top:401px">3.</span>
    <div class="item-icon" role="img" aria-label="Wallet with dollar sign icon" style="left:52px;top:402px"></div>
    <p class="item-text" style="left:135px;top:394px;width:270px"><b>Don't lose or damage your retainer:</b><br>Be careful not to lose or damage your retainer, as replacement will incur an additional fee of $300 per retainer.</p>

    <span class="item-number" style="left:441px;top:401px">4.</span>
    <div class="item-icon" role="img" aria-label="Retainer storage case icon" style="left:478px;top:402px;width:56px"></div>
    <p class="item-text" style="left:562px;top:405px;width:250px"><b>Store retainer properly:</b> Always store your retainer in the provided container.</p>

    <div class="rule" style="left:32px;top:494px;width:785px"></div>

    <span class="item-number" style="left:23px;top:517px">5.</span>
    <div class="item-icon" role="img" aria-label="Toothbrush and cleaner tube icon" style="left:58px;top:513px;width:56px;height:82px"></div>
    <p class="item-text" style="left:137px;top:519px;width:270px"><b>Clean your retainer regularly:</b><br>Use a toothbrush and retainer cleaner (such as CleanSoak) to clean your retainer.</p>

    <span class="item-number" style="left:441px;top:517px">6.</span>
    <div class="item-icon" role="img" aria-label="Retainer with width arrow icon" style="left:474px;top:517px;width:64px;height:76px"></div>
    <p class="item-text" style="left:562px;top:519px;width:260px"><b>Check retainer fit:</b> If your retainer doesn't fit properly, call us to arrange for it to be checked and adjusted.</p>

    <div class="rule" style="left:218px;top:614px;width:413px"></div>

    <span class="item-number" style="left:227px;top:640px">7.</span>
    <div class="item-icon" role="img" aria-label="Appointment calendar icon" style="left:261px;top:636px;width:65px;height:68px"></div>
    <p class="item-text" style="left:350px;top:635px;width:270px"><b>Attend retainer check appointments:</b><br>Regularly attend retainer check appoint-<br>ments to have your retainer tightened.</p>
  </section>

  <section class="clean">
    <div class="clean-band"></div>
    <div class="clean-tab"></div>
    <h2 class="section-heading clean-heading">HOW TO CLEAN A RETAINER:</h2>

    <div class="illustration soak-illus" role="img" aria-label="Retainer soaking in a bowl of warm water with thermometer"></div>
    <p class="clean-text" style="left:211px;top:835px;width:250px">1. <b>Use cleaning tablets:</b><br>Drop one tablet into warm water (not hot), place retainer in solution, and leave for 10-15 minutes.</p>

    <div class="illustration rinse-illus" role="img" aria-label="Retainer rinsed under a running tap"></div>
    <p class="clean-text" style="left:600px;top:835px;width:210px">2. <b>Rinse thoroughly:</b><br>Rinse retainer with running water after cleaning.</p>

    <div class="warning-box"></div>
    <svg class="warning-icon" width="56" height="42" viewBox="0 0 56 42" aria-hidden="true">
      <path d="M28 2 L54 40 H2 Z" fill="var(--warn-yellow)" stroke="#222" stroke-width="2.5" stroke-linejoin="round"/>
      <rect x="26" y="14" width="4" height="14" rx="2" fill="#222"/>
      <circle cx="28" cy="33" r="2.5" fill="#222"/>
    </svg>
    <h3 class="warning-heading">WARNING:</h3>
    <ol class="warning-list">
      <li><b>1. Don't ingest cleaning tablets:</b> Do not place tablets in mouth or use to clean natural teeth.</li>
      <li><b>2. Keep out of reach of children:</b> Keep cleaning tablets out of reach of children.</li>
      <li><b>3. Seek help in case of accidental ingestion:</b> If accidentally ingested, seek professional assistance or contact poison center immediately.</li>
    </ol>
  </section>
</body>
</html>
```